Jewelry Business card for general purpose. Elegant and simple

We are a jewelry group with 6 stores in Mexico and 30 years in business.

We need a BC that at leats includes the name, mail, phone number and physical location (street, municipality, and county; example "Paseo Olmeda 2140", "Avenida Sotillo", "Monterrey").
Optional: we are trying to reposition the brand with the association of life-events or moments and family. Such as: birth, marriage, graduation, birthdays. Christmast, mothers day and fathers day.

We are looking for something elegant but simple

Jewelry name: "Lunetti". Email: "lunettibrillo@correo-ejemplo.mx". Phone num "4172-3095".

Target Market(s)

General business card: from suppliers to clients. One segment outstand: couples gettineg married

Industry/Entity Type

Jewelry Store

Contact Information for Business Card

Loking for something simple but elegant.

Font styles to use
Decorative
Script

Requirements
Must have
• Must have name, address, and mail.
Nice to have
• It could have jewelry pictures/design. Maybe quotes. Or general words as background . currently we have a very simple card with one ring would like to see something different.
Should not have
• Include real people.

```html
<!DOCTYPE html>
<html lang="es">
<head>
<meta charset="utf-8">
<title>Lunetti — Tarjeta de presentación</title>
<link rel="stylesheet" href="https://fonts.googleapis.com/css2?family=Questrial&display=swap">
<style>
  :root {
    --backdrop: #2b1417;
    --card-black: #141414;
    --card-edge: #0b0b0b;
    --gold: #c9a14a;
    --gold-dark: #8a6a24;
    --text-light: #e6e6e6;
    --text-muted: #b9b9b9;
  }
  * { box-sizing: border-box; margin: 0; padding: 0; }
  html, body {
    width: 1200px;
    height: 800px;
    overflow: hidden;
    background: var(--backdrop);
  }
  .canvas {
    position: relative;
    width: 1200px;
    height: 800px;
    display: flex;
    align-items: center;
    justify-content: center;
  }
  .business-card {
    position: relative;
    width: 980px;
    height: 560px;
    background: radial-gradient(ellipse at 60% 40%, #1c1c1c 0%, var(--card-black) 70%);
    border: 1px solid var(--card-edge);
    box-shadow: 0 24px 60px rgba(0, 0, 0, 0.55);
    font-family: "Questrial", "Century Gothic", sans-serif;
  }
  .brand {
    position: absolute;
    left: 120px;
    top: 150px;
    display: flex;
    align-items: center;
    gap: 22px;
  }
  .brand-name {
    font-size: 112px;
    line-height: 1;
    color: var(--gold);
    font-weight: 400;
    letter-spacing: 2px;
  }
  .brand-dot {
    width: 22px;
    height: 22px;
    border-radius: 50%;
    background: var(--gold);
    margin-top: 18px;
  }
  .contact-list {
    position: absolute;
    left: 130px;
    top: 350px;
    list-style: none;
  }
  .contact-item {
    display: flex;
    align-items: center;
    height: 38px;
    font-size: 27px;
    letter-spacing: 0.5px;
    white-space: nowrap;
  }
  .contact-item.is-primary { color: var(--text-light); }
  .contact-item.is-address { color: var(--text-muted); }
  .contact-item.is-continued { padding-left: 44px; }
  .contact-icon {
    flex: none;
    width: 30px;
    height: 30px;
    margin-right: 14px;
  }
</style>
</head>
<body>
  <main class="canvas">
    <section class="business-card" aria-label="Tarjeta de presentación Lunetti">
      <div class="brand">
        <span class="brand-name">Lunetti</span>
        <span class="brand-dot" aria-hidden="true"></span>
      </div>

      <ul class="contact-list">
        <li class="contact-item is-primary">
          <svg class="contact-icon" viewBox="0 0 30 30" aria-hidden="true">
            <circle cx="15" cy="15" r="13" fill="var(--gold-dark)" stroke="var(--gold)" stroke-width="2"/>
            <path d="M10.5 8.5l3 3-1.6 1.8c.9 1.9 2.3 3.3 4.2 4.2l1.8-1.6 3 3-1.8 2c-5 0-10.6-5.6-10.6-10.6z" fill="#111"/>
          </svg>
          4172-3095
        </li>
        <li class="contact-item is-primary">
          <svg class="contact-icon" viewBox="0 0 30 30" aria-hidden="true">
            <circle cx="15" cy="15" r="13" fill="var(--gold-dark)" stroke="var(--gold)" stroke-width="2"/>
            <rect x="8" y="10" width="14" height="10" fill="#111"/>
            <path d="M8 10l7 6 7-6" fill="none" stroke="var(--gold)" stroke-width="1.4"/>
          </svg>
          lunettibrillo@correo-ejemplo.mx
        </li>
        <li class="contact-item is-address">
          <svg class="contact-icon" viewBox="0 0 30 30" aria-hidden="true">
            <circle cx="15" cy="15" r="13" fill="var(--gold-dark)" stroke="var(--gold)" stroke-width="2"/>
            <path d="M15 7a5 5 0 0 0-5 5c0 4 5 10 5 10s5-6 5-10a5 5 0 0 0-5-5z" fill="#111"/>
            <circle cx="15" cy="12" r="1.8" fill="var(--gold)"/>
          </svg>
          Paseo Olmeda 2140
        </li>
        <li class="contact-item is-address is-continued">Local 14, Avenida Sotillo</li>
      </ul>
    </section>
  </main>
</body>
</html>
```